Flyer for annual KESTREL SUMMIT 2020

I would like a church event flyer designed. The event is called "KESTREL SUMMIT 2020". I am looking for a professional, yet catchy design that uses our brand colors and logo creatively while communicating key information of the event effectively.

1. The logo is attached in two color formats. The designer has the choice to use them as he/she want.

2. The location of the event is: Harlow Community Center, 239 Fennimore Street, Portland, ME 04117

3. Time and date of event. The designer can organize and format the date and time as he/she pleases.
Thursday December 31st @ 6:30PM
Friday January 1st @ 6:30PM
Saturday 2nd @ 6:30PM
Sunday 3rd @ 4:30PM

4. The topic of the event is "In Fire and On Fire". The designer is free to use this phrase as he/she pleases to create a good composition.

5. Speaker: Prophet Marcus Olunde (2 pictures of the speaker to choose from are attached)

6. Contact information: contact@brightmeadowfold.org - Telephone number: 207 583 2914

7. I would also like the following three words on the flyer. These words describe the focus of the event: FIRE, REVIVAL, PROPHETIC

Target Market(s)

Young adults

Font styles to use
Sans Serif

Requirements
Must have
• Logo, speaker's picture
Should not have
• cross image, church image

```html
<!DOCTYPE html>
<html lang="en">
<head>
<meta charset="utf-8">
<title>Kestrel Summit 2020 Flyer</title>
<link rel="stylesheet" href="https://fonts.googleapis.com/css2?family=Montserrat:wght@400;600;700;800&family=Poppins:wght@400;600;700&display=swap">
<style>
  :root {
    --navy: #123a5f;
    --navy-ink: #14375a;
    --dusk: #4a4556;
    --amber: #a86a3e;
    --orange: #f7941d;
    --bronze: #9a6a34;
    --white: #ffffff;
    --pill: #463f4d;
    --ghost: rgba(255, 255, 255, 0.14);
    --page: #ffffff;
  }
  * { box-sizing: border-box; margin: 0; padding: 0; }
  html, body {
    width: 1181px; height: 1200px; overflow: hidden;
    background: var(--page);
  }
  .flyer {
    position: absolute; left: 200px; top: 49px;
    width: 782px; height: 1102px; overflow: hidden;
    background: linear-gradient(180deg, var(--navy) 0%, #1c3c5e 30%, var(--dusk) 50%, var(--amber) 70%, #e88a28 88%, var(--orange) 100%);
    font-family: "Montserrat", sans-serif;
    color: var(--white);
  }
  .brand {
    position: absolute; left: 34px; top: 62px;
    display: flex; align-items: center; gap: 10px;
    font-family: "Montserrat", sans-serif; font-weight: 700;
    font-size: 38px; letter-spacing: 1px; color: var(--white);
  }
  .brand-dot { width: 14px; height: 14px; border-radius: 50%; background: var(--orange); }
  .theme-band {
    position: absolute; left: 0; top: 151px; width: 220px; height: 100px;
    background: linear-gradient(90deg, var(--bronze) 0%, rgba(154,106,52,0.55) 60%, rgba(154,106,52,0) 100%);
    display: flex; flex-direction: column; align-items: center; justify-content: center;
    padding-right: 10px; line-height: 1;
  }
  .theme-band .big { font-size: 29px; font-weight: 600; }
  .theme-band .small { font-size: 18px; font-weight: 400; margin: 2px 0; }
  .focus-words {
    position: absolute; right: 58px; top: 30px; text-align: right;
    font-weight: 700; font-size: 84px; line-height: 104px;
    letter-spacing: 10px; color: var(--ghost); filter: blur(1.2px);
  }
  .speaker-photo {
    position: absolute; left: 400px; top: 300px; right: 0; bottom: 0;
    border-radius: 180px 0 0 0;
    background: linear-gradient(180deg, #3a2e33 0%, #7a3a2a 35%, #c8512c 70%, #b84526 100%);
  }
  .title { position: absolute; left: 32px; top: 400px; line-height: 1; text-shadow: 0 2px 6px rgba(0,0,0,0.25); }
  .title .event { display: block; font-size: 72px; font-weight: 800; }
  .title .kind { display: block; font-size: 54px; font-weight: 800; margin-top: 22px; }
  .title .year { display: block; font-size: 68px; font-weight: 400; margin-top: 24px; }
  .rule { position: absolute; left: 0; width: 367px; height: 2px; background: var(--navy-ink); }
  .info { position: absolute; left: 34px; color: var(--navy-ink); }
  .icon { position: absolute; left: 0; }
  .venue { top: 770px; }
  .venue .name { margin-left: 37px; font-size: 16px; font-weight: 700; white-space: nowrap; }
  .venue .addr { margin-left: 37px; font-family: "Poppins", sans-serif; font-size: 13.5px; margin-top: 3px; white-space: nowrap; }
  .schedule { top: 855px; }
  .schedule li { list-style: none; margin-left: 37px; font-size: 19px; font-weight: 700; line-height: 31px; }
  .contact { top: 1004px; font-weight: 700; width: 340px; }
  .contact p { margin-left: 37px; line-height: 30px; white-space: nowrap; }
  .contact .phone { font-size: 17.5px; }
  .contact .email { font-size: 14px; }
  .speaker-name {
    position: absolute; left: 409px; top: 997px; width: 373px; height: 62px;
    border-radius: 31px 0 0 31px; background: var(--pill);
    display: flex; align-items: center; justify-content: center;
    font-family: "Poppins", sans-serif; font-weight: 700; font-size: 21px; color: var(--white);
  }
</style>
</head>
<body>
  <main class="flyer">
    <div class="brand"><span class="brand-dot"></span>VARNELL</div>

    <div class="theme-band">
      <span class="big">IN FIRE</span>
      <span class="small">AND</span>
      <span class="big">ON FIRE</span>
    </div>

    <div class="focus-words">FIRE<br>REVIVAL<br>PROPHETIC</div>

    <div class="speaker-photo" role="img" aria-label="Photo of the speaker in a red-orange suit jacket"></div>

    <h1 class="title">
      <span class="event">KESTREL</span>
      <span class="kind">SUMMIT</span>
      <span class="year">2020</span>
    </h1>

    <div class="rule" style="top:756px"></div>
    <div class="info venue">
      <svg class="icon" style="top:2px" width="28" height="40" viewBox="0 0 28 40" fill="none" stroke="#14375a" stroke-width="2">
        <path d="M14 38 C6 26 2 20 2 14 A12 12 0 0 1 26 14 C26 20 22 26 14 38 Z"/>
        <circle cx="14" cy="14" r="5"/>
      </svg>
      <p class="name">HARLOW COMMUNITY CENTER</p>
      <p class="addr">239 Fennimore Street, Portland, ME 04117</p>
    </div>

    <div class="rule" style="top:834px"></div>
    <div class="info schedule">
      <svg class="icon" style="top:48px" width="28" height="30" viewBox="0 0 28 30" fill="none" stroke="#14375a" stroke-width="2">
        <rect x="2" y="6" width="24" height="22" rx="2"/>
        <line x1="2" y1="12" x2="26" y2="12"/>
        <line x1="8" y1="2" x2="8" y2="8"/><line x1="20" y1="2" x2="20" y2="8"/>
        <g fill="#14375a" stroke="none">
          <rect x="6" y="16" width="3" height="3"/><rect x="12.5" y="16" width="3" height="3"/><rect x="19" y="16" width="3" height="3"/>
          <rect x="6" y="21" width="3" height="3"/><rect x="12.5" y="21" width="3" height="3"/><rect x="19" y="21" width="3" height="3"/>
        </g>
      </svg>
      <ul>
        <li>THU DEC 31ST @ 6:30PM</li>
        <li>FRI JAN 1ST @ 6:30PM</li>
        <li>SAT JAN 2ND @ 6:30PM</li>
        <li>SUN JAN 3RD @ 4:30PM</li>
      </ul>
    </div>

    <div class="rule" style="top:984px"></div>
    <div class="info contact">
      <svg class="icon" style="top:2px" width="26" height="26" viewBox="0 0 26 26">
        <rect width="26" height="26" rx="5" fill="#14375a"/>
        <path d="M8 6 L11 6 L12 10 L10 11.5 C11 14 12 15 14.5 16 L16 14 L20 15 L20 18 C20 19 19 20 18 20 C11 19.5 6.5 15 6 8 C6 7 7 6 8 6 Z" fill="#f7941d"/>
      </svg>
      <p class="phone">207 583 2914</p>
      <svg class="icon" style="top:32px" width="26" height="26" viewBox="0 0 26 26">
        <circle cx="13" cy="13" r="13" fill="#14375a"/>
        <text x="13" y="18" text-anchor="middle" font-family="Montserrat, sans-serif" font-weight="700" font-size="15" fill="#f7941d">@</text>
      </svg>
      <p class="email">CONTACT@BRIGHTMEADOWFOLD.ORG</p>
    </div>
    <div class="rule" style="top:1081px"></div>

    <div class="speaker-name">PROPHET MARCUS OLUNDE</div>
  </main>
</body>
</html>
```